VerintaCore PowerPoint Presentation Design

I am looking for a PowerPoint design for a new company based in Dallas, Texas called VerintaCore. We provide extremely powerful predictive and prescriptive analytics software focused on the Internet of Things (IoT) market. Our initial products are called VRC Foundry and VRC Pulse. We would like to see designs that support our logo design, which is attached.

I AM LOOKING FOR A THEME TO BE DEVELOPED FOR THE TITLE SLIDE AND INSIDE SLIDES OF A PRESENTATION. I AM NOT LOOKING FOR SOMEONE TO TAKE MY CONTENT AND CREATE A COMPLETE PRESENTATION.

Target Market(s)

Advanced Analytics, Internet of Things

Industry/Entity Type

It Company

Requirements
Must have
• Bolder colors, but they must work with the logo
Nice to have
• I prefer that the design incorporate the them of "connectivity" or "connectedness" to reflect the IoT market and "intelligence" or "smart" to reflect the analytics aspect of the business
Should not have
• I don't want people represented in the graphics scheme

```html
<!DOCTYPE html>
<html lang="en">
<head>
<meta charset="utf-8">
<title>VerintaCore Presentation Theme</title>
<link href="https://fonts.googleapis.com/css2?family=Signika:wght@400;600;700&family=Open+Sans:wght@400;600&display=swap" rel="stylesheet">
<style>
:root{
  --blue:#0d4fa8;
  --blue-deep:#0a3f8f;
  --orange:#f5a623;
  --orange-light:#f9c01a;
  --ink:#111111;
  --text:#6d6d6d;
  --paper:#efefef;
  --line:#cfcfcf;
  --canvas:#000000;
}
*{box-sizing:border-box;margin:0;padding:0}
html,body{width:1058px;height:1200px;overflow:hidden;background:var(--canvas)}
body{position:relative;font-family:"Open Sans",Arial,sans-serif}
.slide{position:absolute;width:506px;height:380px;background:var(--paper);overflow:hidden}
.slide > *{position:absolute}
.col-left{left:20px}.col-right{left:535px}
.row-1{top:18px}.row-2{top:409px}.row-3{top:800px}

.brand{font-family:"Signika",sans-serif;font-weight:600;color:var(--blue);letter-spacing:-.2px;line-height:1}
.brand-corner{right:14px;top:10px;font-size:19px}

.slide-title{left:21px;top:12px;font-family:"Signika",sans-serif;font-weight:700;font-size:17px;color:var(--ink);letter-spacing:.2px}
.slide-title span{color:var(--blue)}
.title-rule{left:21px;top:33px;width:200px;height:1px;background:var(--line)}
.slide-sub{left:21px;top:38px;font-size:8.5px;color:var(--text)}

.lorem{font-size:7.8px;line-height:13.8px;color:var(--text)}
.lorem em{font-style:normal;color:var(--blue)}
.heading-blue{font-family:"Signika",sans-serif;font-size:12.5px;color:var(--blue)}

.footer{left:0;bottom:0;width:506px;height:26px}
.footer-copy{left:6px;bottom:7px;font-size:7.5px;color:#fff}
.footer-page{right:10px;bottom:7px;font-size:7.5px;color:#fff}

/* title slide */
.cover-top{left:0;top:0;width:506px;height:207px;background:var(--paper)}
.cover-rule{left:0;top:207px;width:506px;height:3px;background:var(--blue)}
.cover-band{left:0;top:210px;width:506px;height:170px;background:var(--orange)}
.cover-brand{left:0;width:506px;top:144px;text-align:center;font-size:48px}
.cover-title{left:0;width:506px;top:261px;text-align:center;font-family:"Signika",sans-serif;font-weight:700;font-size:23px;color:var(--ink)}
.cover-sub{left:123px;width:260px;top:296px;text-align:center;font-size:9px;line-height:14px;color:var(--ink)}

/* feature columns */
.feature{width:150px;top:103px;text-align:center}
.feature .tick{display:block;margin:0 auto 10px;width:44px;height:44px}
.feature .heading-blue{display:block;margin-bottom:4px}

/* team rows */
.portrait{left:49px;width:108px;height:108px;border-radius:50%;border:1px solid #555;background:radial-gradient(circle at 45% 40%,#d9d9d9,#8a8a8a 70%,#4a4a4a)}
.member{left:161px;width:330px}
.member .heading-blue{display:block;margin-bottom:4px}
.member p + p{margin-top:4px}

/* contact slide */
.contact{background:radial-gradient(circle at 80% 20%,#2a6bd0 0%,var(--blue) 45%,var(--blue-deep) 100%)}
.contact-brand{left:18px;top:169px;font-size:37px;color:#fff}
.contact-card{left:272px;top:122px;width:234px;height:134px;background:#fff;padding:10px 13px}
.contact-card p{position:static;font-size:12px;line-height:16px;color:#333}
.contact-list{list-style:none;margin-top:10px}
.contact-list li{display:flex;align-items:center;gap:8px;font-size:12px;line-height:16px;color:#333}
.contact-list svg{width:12px;height:12px;flex:none}

/* timeline */
.intro{left:21px;top:64px;width:470px}
.timeline-line{left:91px;top:144px;width:320px;height:2px;background:var(--orange)}
.year{width:42px;height:42px;border-radius:50%;border:3px solid #ddd;top:124px;color:#fff;font-family:"Signika",sans-serif;font-weight:700;font-size:13px;display:flex;align-items:center;justify-content:center}
.card{top:170px;width:141px;height:168px;background:#fff;border:1px solid}
.card-head{height:26px;color:#fff;font-family:"Signika",sans-serif;font-weight:700;font-size:10px;display:flex;align-items:center;justify-content:center}
.card .lorem{padding:8px 14px}
.tone-blue{background:var(--blue);border-color:var(--blue)}
.tone-orange{background:var(--orange);border-color:var(--orange)}
.tone-black{background:var(--ink);border-color:var(--ink)}

/* bullet list */
.point{left:26px;width:470px}
.point svg{position:absolute;left:0;top:1px;width:10px;height:13px}
.point .heading-blue{display:block;margin-left:16px;font-size:11.5px;margin-bottom:3px}
.point .lorem{margin-left:16px}
</style>
</head>
<body>

<!-- Title slide -->
<section class="slide col-left row-1">
  <div class="cover-top"></div>
  <div class="cover-rule"></div>
  <div class="cover-band"></div>
  <div class="brand cover-brand">VerintaCore</div>
  <h1 class="cover-title">Project Title Here</h1>
  <p class="cover-sub">Subtext here Subtext here Subtext here Subtext here Subtext here Subtext here Subtext here</p>
</section>

<!-- Team features slide -->
<section class="slide col-right row-1">
  <h2 class="slide-title">OUR <span>TEAM</span></h2>
  <div class="title-rule"></div>
  <p class="slide-sub">Subtext here Subtext here Subtext here</p>
  <div class="brand brand-corner">VerintaCore</div>

  <div class="feature" style="left:13px">
    <svg class="tick" viewBox="0 0 44 44"><circle cx="22" cy="22" r="22" fill="#111"/><rect x="15.5" y="15.5" width="13" height="13" rx="2" fill="#fff"/><path d="M18.5 22l2.6 2.6 4.6-5" stroke="#111" stroke-width="2" fill="none"/></svg>
    <span class="heading-blue">Text Title Here</span>
    <p class="lorem">Lorem ipsum dolor sit Lorem ipsum dolor sit Lorem ipsum dolor sit Lorem ipsum dolor sit Lorem ipsum dolor sit Lorem ipsum dolor sit Lorem ipsum dolor sit Lorem ipsum dolor sit Lorem ipsum dolor sit Lorem ipsum dolor sit Lorem ipsum dolor sit</p>
  </div>
  <div class="feature" style="left:180px">
    <svg class="tick" viewBox="0 0 44 44"><circle cx="22" cy="22" r="22" fill="#111"/><rect x="15.5" y="15.5" width="13" height="13" rx="2" fill="#fff"/><path d="M18.5 22l2.6 2.6 4.6-5" stroke="#111" stroke-width="2" fill="none"/></svg>
    <span class="heading-blue">Text Title Here</span>
    <p class="lorem">Lorem ipsum dolor sit Lorem ipsum dolor sit Lorem ipsum dolor sit Lorem ipsum dolor sit Lorem ipsum dolor sit Lorem ipsum dolor sit Lorem ipsum dolor sit Lorem ipsum dolor sit Lorem ipsum dolor sit Lorem ipsum dolor sit Lorem ipsum dolor sit</p>
  </div>
  <div class="feature" style="left:349px">
    <svg class="tick" viewBox="0 0 44 44"><circle cx="22" cy="22" r="22" fill="#111"/><rect x="15.5" y="15.5" width="13" height="13" rx="2" fill="#fff"/><path d="M18.5 22l2.6 2.6 4.6-5" stroke="#111" stroke-width="2" fill="none"/></svg>
    <span class="heading-blue">Text Title Here</span>
    <p class="lorem">Lorem ipsum dolor sit Lorem ipsum dolor sit Lorem ipsum dolor sit Lorem ipsum dolor sit Lorem ipsum dolor sit Lorem ipsum dolor sit Lorem ipsum dolor sit Lorem ipsum dolor sit Lorem ipsum dolor sit Lorem ipsum dolor sit Lorem ipsum dolor sit</p>
  </div>

  <svg class="footer" viewBox="0 0 506 26"><defs><linearGradient id="bar1" x1="0" x2="1"><stop offset="0" stop-color="#f5a623"/><stop offset="1" stop-color="#f9c01a"/></linearGradient></defs><polygon points="0,0 448,0 458,26 0,26" fill="url(#bar1)"/><polygon points="456,0 468,0 478,26 466,26" fill="#111"/><polygon points="466,0 506,0 506,26 476,26" fill="#1f4bb0"/></svg>
  <span class="footer-copy">Copyright text here</span>
  <span class="footer-page">01</span>
</section>

<!-- Team profiles slide -->
<section class="slide col-left row-2">
  <h2 class="slide-title">OUR <span>TEAM</span></h2>
  <div class="title-rule"></div>
  <p class="slide-sub">Subtext here Subtext here Subtext here</p>
  <div class="brand brand-corner">VerintaCore</div>

  <div class="portrait" style="top:73px" role="img" aria-label="Portrait photo of a director"></div>
  <div class="member" style="top:79px">
    <span class="heading-blue">Director Name Here</span>
    <p class="lorem">Lorem ipsum dolor sit Lorem ipsum dolor sit Lorem ipsum dolor sit Lorem ipsum dolor sit Lorem ipsum dolor sit Lorem ipsum dolor <em>sit Lorem ipsum dolor sit Lorem ipsum dolor sit Lorem ipsum dolor sit Lorem ipsum dolor sit</em></p>
    <p class="lorem">Lorem ipsum dolor sit Lorem ipsum dolor sit Lorem ipsum dolor sit Lorem ipsum dolor sit Lorem ipsum dolor sit Lorem ipsum dolor sit Lorem ipsum dolor sit Lorem ipsum dolor sit</p>
  </div>

  <div class="portrait" style="top:212px" role="img" aria-label="Portrait photo of a director"></div>
  <div class="member" style="top:217px">
    <span class="heading-blue">Director Name Here</span>
    <p class="lorem">Lorem ipsum dolor sit Lorem ipsum dolor sit Lorem ipsum dolor sit Lorem ipsum dolor sit Lorem ipsum dolor sit Lorem ipsum dolor <em>sit Lorem ipsum dolor sit Lorem ipsum dolor sit Lorem ipsum dolor sit Lorem ipsum dolor sit</em></p>
    <p class="lorem">Lorem ipsum dolor sit Lorem ipsum dolor sit Lorem ipsum dolor sit Lorem ipsum dolor sit Lorem ipsum dolor sit Lorem ipsum dolor sit Lorem ipsum dolor sit Lorem ipsum dolor sit</p>
  </div>

  <svg class="footer" viewBox="0 0 506 26"><defs><linearGradient id="bar2" x1="0" x2="1"><stop offset="0" stop-color="#f5a623"/><stop offset="1" stop-color="#f9c01a"/></linearGradient></defs><polygon points="0,0 448,0 458,26 0,26" fill="url(#bar2)"/><polygon points="456,0 468,0 478,26 466,26" fill="#111"/><polygon points="466,0 506,0 506,26 476,26" fill="#1f4bb0"/></svg>
  <span class="footer-copy">Copyright text here</span>
  <span class="footer-page">01</span>
</section>

<!-- Contact slide -->
<section class="slide contact col-right row-2">
  <div class="brand contact-brand">VerintaCore</div>
  <div class="contact-card">
    <p>Lorem ipsum dolor sit amet, consectetur adipiscing elit. Donec accumsan.</p>
    <ul class="contact-list">
      <li><svg viewBox="0 0 12 12"><path d="M3 1l2 2.5-1 1.3c.6 1.3 1.5 2.2 2.8 2.8L8.1 6.6 10.6 8.6 9.6 10.8C5 10.4 1.4 6.8 1.2 2.2z" fill="#333"/></svg>: 555 0142 7730</li>
      <li><svg viewBox="0 0 12 12"><rect x="1" y="2.5" width="10" height="7" fill="#333"/><path d="M1.3 2.8L6 6.6l4.7-3.8" stroke="#fff" stroke-width="1" fill="none"/></svg>: hello@verintacore.io</li>
      <li><svg viewBox="0 0 12 12"><path d="M11 1L1 5.5l4 1.5 1.5 4z" fill="#333"/></svg>: verintacore.io</li>
    </ul>
  </div>
</section>

<!-- About timeline slide -->
<section class="slide col-left row-3">
  <h2 class="slide-title">ABOUT US <span>VERINTACORE</span></h2>
  <div class="title-rule"></div>
  <p class="slide-sub">Subtext here Subtext here Subtext here</p>
  <div class="brand brand-corner">VerintaCore</div>
  <p class="lorem intro">Lorem ipsum dolor sit Lorem ipsum dolor sit Lorem ipsum dolor sit Lorem ipsum dolor sit Lorem ipsum dolor sit Lorem ipsum dolor sit Lorem ipsum dolor sit Lorem ipsum dolor sit Lorem ipsum dolor sit Lorem ipsum dolor sit Lorem ipsum dolor sit Lorem ipsum dolor sit Lorem ipsum dolor sit Lorem ipsum dolor sit Lorem ipsum dolor sit</p>

  <div class="timeline-line"></div>
  <div class="year tone-blue" style="left:70px;border-color:#ddd">1995</div>
  <div class="year tone-orange" style="left:229px;border-color:#ddd">2005</div>
  <div class="year tone-black" style="left:390px;border-color:#ddd">2015</div>

  <div class="card" style="left:22px;border-color:var(--blue)"><div class="card-head tone-blue">TITLE HERE</div><p class="lorem">Lorem ipsum dolor sit Lorem ipsum dolor sit Lorem ipsum dolor sit Lorem ipsum dolor sit Lorem ipsum dolor sit Lorem ipsum dolor sit Lorem ipsum dolor sit Lorem ipsum dolor sit Lorem ipsum dolor sit Lorem ipsum dolor sit</p></div>
  <div class="card" style="left:181px;border-color:var(--orange)"><div class="card-head tone-orange">TITLE HERE</div><p class="lorem">Lorem ipsum dolor sit Lorem ipsum dolor sit Lorem ipsum dolor sit Lorem ipsum dolor sit Lorem ipsum dolor sit Lorem ipsum dolor sit Lorem ipsum dolor sit Lorem ipsum dolor sit Lorem ipsum dolor sit Lorem ipsum dolor sit</p></div>
  <div class="card" style="left:341px;border-color:var(--ink)"><div class="card-head tone-black">TITLE HERE</div><p class="lorem">Lorem ipsum dolor sit Lorem ipsum dolor sit Lorem ipsum dolor sit Lorem ipsum dolor sit Lorem ipsum dolor sit Lorem ipsum dolor sit Lorem ipsum dolor sit Lorem ipsum dolor sit Lorem ipsum dolor sit Lorem ipsum dolor sit</p></div>

  <svg class="footer" viewBox="0 0 506 26"><defs><linearGradient id="bar3" x1="0" x2="1"><stop offset="0" stop-color="#f5a623"/><stop offset="1" stop-color="#f9c01a"/></linearGradient></defs><polygon points="0,0 448,0 458,26 0,26" fill="url(#bar3)"/><polygon points="456,0 468,0 478,26 466,26" fill="#111"/><polygon points="466,0 506,0 506,26 476,26" fill="#1f4bb0"/></svg>
  <span class="footer-copy">Copyright text here</span>
  <span class="footer-page">01</span>
</section>

<!-- About list slide -->
<section class="slide col-right row-3">
  <h2 class="slide-title">ABOUT US <span>VERINTACORE</span></h2>
  <div class="title-rule"></div>
  <p class="slide-sub">Subtext here Subtext here Subtext here</p>
  <div class="brand brand-corner">VerintaCore</div>

  <div class="point" style="top:73px"><svg viewBox="0 0 10 13"><path d="M1 1l7 5.5L1 12" stroke="#f5a623" stroke-width="2.4" fill="none"/></svg><span class="heading-blue">Lorem ipsum dolor sit Lorem ipsum</span><p class="lorem">Lorem ipsum dolor sit Lorem ipsum dolor sit Lorem ipsum dolor sit Lorem ipsum dolor sit Lorem ipsum dolor sit Lorem ipsum dolor sit Lorem ipsum dolor sit Lorem ipsum dolor sit Lorem ipsum dolor sit Lorem ipsum</p></div>
  <div class="point" style="top:131px"><svg viewBox="0 0 10 13"><path d="M1 1l7 5.5L1 12" stroke="#f5a623" stroke-width="2.4" fill="none"/></svg><span class="heading-blue">Lorem ipsum dolor sit Lorem ipsum</span><p class="lorem">Lorem ipsum dolor sit Lorem ipsum dolor sit Lorem ipsum dolor sit Lorem ipsum dolor sit Lorem ipsum dolor sit Lorem ipsum dolor sit Lorem ipsum dolor sit Lorem ipsum dolor sit Lorem ipsum dolor sit Lorem ipsum</p></div>
  <div class="point" style="top:195px"><svg viewBox="0 0 10 13"><path d="M1 1l7 5.5L1 12" stroke="#f5a623" stroke-width="2.4" fill="none"/></svg><span class="heading-blue">Lorem ipsum dolor sit Lorem ipsum</span><p class="lorem">Lorem ipsum dolor sit Lorem ipsum dolor sit Lorem ipsum dolor sit Lorem ipsum dolor sit Lorem ipsum dolor sit Lorem ipsum dolor sit Lorem ipsum dolor sit Lorem ipsum dolor sit Lorem ipsum dolor sit Lorem ipsum</p></div>
  <div class="point" style="top:259px"><svg viewBox="0 0 10 13"><path d="M1 1l7 5.5L1 12" stroke="#f5a623" stroke-width="2.4" fill="none"/></svg><span class="heading-blue">Lorem ipsum dolor sit Lorem ipsum</span><p class="lorem">Lorem ipsum dolor sit Lorem ipsum dolor sit Lorem ipsum dolor sit Lorem ipsum dolor sit Lorem ipsum dolor sit Lorem ipsum dolor sit Lorem ipsum dolor sit Lorem ipsum dolor sit Lorem ipsum dolor sit Lorem ipsum</p></div>

  <svg class="footer" viewBox="0 0 506 26"><defs><linearGradient id="bar4" x1="0" x2="1"><stop offset="0" stop-color="#f5a623"/><stop offset="1" stop-color="#f9c01a"/></linearGradient></defs><polygon points="0,0 448,0 458,26 0,26" fill="url(#bar4)"/><polygon points="456,0 468,0 478,26 466,26" fill="#111"/><polygon points="466,0 506,0 506,26 476,26" fill="#1f4bb0"/></svg>
  <span class="footer-copy">Copyright text here</span>
  <span class="footer-page">01</span>
</section>

</body>
</html>
```